Media/PR business needs a website upgrade

Modernise my website www.vrl.net.au into a simpler and mobile friendly site with the usual plugins, maximum 5 pages, 4 might be enough. My page is already hosted and I have an email address so I just want to work with a designer who is fantastic with WordPress, to refresh and simplify the 6 year-old look.

Target Market(s)

men & women 25-55

Industry/Entity Type

Business

Coding

Coded - Design and coding required

Number of Pages Required

4 page

Font styles to use
Sans Serif

Colors
f37122
ffffff

Requirements
Must have
• Social media plugins, about, client portfolio, contact (can be under about)blog capability
Nice to have
• photos of jobs I've done
Should not have
• e-commerce, can lose all the client logos

```html
<!DOCTYPE html>
<html lang="en">
<head>
<meta charset="utf-8">
<title>Vantage Relations Lab – Public Relations & Event Management</title>
<link href="https://fonts.googleapis.com/css2?family=Questrial&family=Open+Sans:wght@400;600;700&display=swap" rel="stylesheet">
<style>
:root{
  --orange:#f37122;
  --white:#ffffff;
  --ink:#333333;
  --muted:#555555;
  --soft-bg:#eef1f4;
  --footer:#4a4a4a;
  --footer-deep:#3a3a3a;
  --line:#dddddd;
}
*{box-sizing:border-box;margin:0;padding:0}
html,body{width:1200px;height:3574px;overflow:hidden}
body{background:var(--white);color:var(--ink);font-family:"Open Sans",Arial,sans-serif;font-size:12px;line-height:1.7;position:relative}
.abs{position:absolute}
.heading{font-family:"Questrial","Open Sans",sans-serif;font-weight:400}
.btn{display:inline-block;background:var(--orange);color:var(--white);font-size:11px;font-weight:600;text-transform:uppercase;letter-spacing:.5px;text-align:center;line-height:40px;width:128px;height:40px;text-decoration:none}
.btn-outline{display:inline-block;border:1.5px solid var(--white);color:var(--white);font-size:10px;font-weight:600;text-transform:uppercase;width:92px;height:38px;line-height:35px;text-align:center}

/* header */
.site-header{left:0;top:0;width:1200px;height:96px;background:var(--white)}
.brand{left:130px;top:20px;display:flex;align-items:center;gap:10px}
.brand-dot{width:54px;height:54px;border-radius:50%;background:var(--orange)}
.brand-name{font-family:"Questrial",sans-serif;font-size:16px;line-height:1.1;color:var(--ink);width:130px}
.social-top{left:818px;top:18px;display:flex;gap:10px}
.social-dot{width:11px;height:11px;border-radius:50%;background:#8a8a8a}
.phone{left:930px;top:12px;display:flex;align-items:center;gap:6px;font-family:"Questrial",sans-serif;font-size:21px;color:var(--ink)}
.main-nav{left:520px;top:62px;display:flex;gap:24px;font-size:13px;color:var(--ink)}
.main-nav .active{color:var(--ink);border-bottom:2px solid var(--orange);padding-bottom:8px}

/* hero */
.hero{left:0;top:96px;width:1200px;height:618px;background:linear-gradient(90deg,#d8d0c3 0%,#cfc6b8 45%,#b9b2a6 70%,#8e8c88 100%)}
.hero-portrait{left:580px;top:0;width:620px;height:618px;background:linear-gradient(180deg,#b7ad9e 0%,#9a8f80 40%,#3d6fa8 72%,#3466a0 100%)}
.hero-copy{left:140px;top:180px;width:560px}
.hero-title{font-size:38px;line-height:1.2;color:#1e1e1e;font-weight:600;font-family:"Questrial",sans-serif}
.hero-sub{font-family:"Questrial",sans-serif;font-size:20px;color:#2a2a2a;margin:12px 0 22px;line-height:1.35}

/* intro */
.intro-title{left:140px;top:800px;width:500px;font-size:26px;line-height:1.42;color:var(--orange)}
.intro-text{left:140px;top:928px;width:480px;font-size:12px;color:var(--muted)}
.intro-text p{margin-bottom:14px}
.intro-cols{left:140px;top:1155px;display:flex;gap:62px;font-size:10px;font-weight:700;color:var(--ink);line-height:1.3;text-transform:uppercase}
.intro-btn{left:140px;top:1217px}
.collage{background:linear-gradient(135deg,#9aa3ad,#5f6873)}

/* expertise */
.section-title{width:1200px;text-align:center;color:var(--orange);font-size:24px}
.expertise-grid{left:0;top:1450px;width:1200px;height:485px;display:grid;grid-template-columns:repeat(4,300px);grid-template-rows:repeat(2,242.5px)}
.tile{display:flex;flex-direction:column;align-items:center;justify-content:center;gap:14px;color:var(--white);text-align:center}
.tile h3{font-family:"Questrial",sans-serif;font-weight:400;font-size:16px;line-height:1.25;max-width:230px}

/* blog */
.blog-intro{left:140px;top:2090px;width:270px}
.blog-intro h2{font-family:"Questrial",sans-serif;font-weight:600;font-size:24px;line-height:1.2;text-transform:uppercase;color:#222}
.blog-intro p{color:var(--muted);font-size:11.5px;margin:8px 0 20px}
.post{width:292px}
.post-img{width:292px;height:190px}
.post-title{color:var(--orange);font-size:11.5px;margin-top:12px}
.post-meta{color:#888;font-size:9.5px}
.post-more{font-size:9.5px;font-weight:700;color:#333}

/* about */
.about{left:0;top:2450px;width:1200px;height:545px;background:var(--soft-bg)}
.about .section-title{position:absolute;top:40px}
.about-lead{top:82px;width:1200px;text-align:center;font-size:22px;color:#222}
.about-text{left:200px;top:128px;width:800px;text-align:center;font-size:11.5px;color:var(--muted)}
.about-text p{margin-bottom:16px}
.pillars{left:200px;top:290px;width:800px;display:flex;justify-content:space-between}
.pillar{width:240px;text-align:center;font-size:11px;color:var(--muted)}
.pillar h4{font-size:12px;font-weight:600;color:#222;text-transform:uppercase;margin:8px 0 6px}
.about-btn{left:536px;top:473px}

/* clients */
.clients .section-title{color:#333}
.client-row{left:195px;top:3130px;width:810px;display:flex;justify-content:space-between;align-items:center}
.client-badge{background:#d9dde2}

/* footer */
.site-footer{left:0;top:3260px;width:1200px;height:314px;background:var(--footer);color:#e6e6e6}
.footer-brand{left:140px;top:30px;display:flex;align-items:center;gap:10px}
.footer-brand .brand-name{color:var(--white)}
.footer-social{left:212px;top:113px;display:flex;gap:10px}
.footer-social .social-dot{background:#bbbbbb}
.footer-list{font-size:10px;line-height:2.35;list-style:none}
.contact-block{left:752px;top:30px;font-size:10px;line-height:2.1}
.contact-block dt{display:inline-block;width:40px}
.contact-block dd{display:inline}
.footer-bottom{left:130px;top:225px;width:940px;height:75px;background:var(--footer-deep);font-size:9.5px;display:flex;justify-content:space-between;align-items:center;padding:0 24px 0 28px}
.footer-bottom nav{display:flex;gap:28px}
</style>
</head>
<body>

<header class="site-header abs">
  <div class="brand abs">
    <div class="brand-dot"></div>
    <div class="brand-name">Vantage Relations Lab</div>
  </div>
  <div class="social-top abs" aria-label="Social links">
    <span class="social-dot"></span><span class="social-dot"></span><span class="social-dot"></span><span class="social-dot"></span>
  </div>
  <div class="phone abs">
    <svg width="16" height="16" viewBox="0 0 24 24" aria-hidden="true"><path fill="#333" d="M6.6 10.8a15 15 0 0 0 6.6 6.6l2.2-2.2c.3-.3.7-.4 1-.2 1.1.4 2.3.6 3.6.6.6 0 1 .4 1 1V20c0 .6-.4 1-1 1A17 17 0 0 1 3 4c0-.6.4-1 1-1h3.5c.6 0 1 .4 1 1 0 1.3.2 2.5.6 3.6.1.3 0 .7-.2 1z"/></svg>
    0400 216 730
  </div>
  <nav class="main-nav abs">
    <span class="active">Home</span><span>Services</span><span>About</span><span>Client Portfolio</span><span>Testimonials</span><span>Blog</span><span>Contact</span>
  </nav>
</header>

<section class="hero abs">
  <div class="hero-portrait abs" role="img" aria-label="Photograph of the business founder in a blue sailing top and light jacket"></div>
  <div class="hero-copy abs">
    <h1 class="hero-title">Public Relations &amp;<br>Event Management Business</h1>
    <p class="hero-sub">Flexible, composed and relationship focused<br>freelancer ready to start work.</p>
    <a class="btn">Learn More</a>
  </div>
</section>

<section class="intro">
  <h2 class="intro-title heading abs">Vantage Relations Lab is an established specialist public relations and event management business.</h2>
  <div class="intro-text abs">
    <p>With a communications degree and 20 plus years experience working in public relations, publicity, media and project management, VRL founder Mara Whitley offers a complete contract based option for your next major sporting, social, cultural or community event.</p>
    <p>Contact Mara at VRL for strategic advice on sponsorship spend and how to leverage your investment, and to tap into her extensive media and professional network.</p>
    <p>Flexible, composed and relationship focused freelancer ready to start work.</p>
  </div>
  <div class="intro-cols abs">
    <span>Contrary to<br>popular belief</span><span>Lorem ipsum<br>is simply dummy</span><span>Map lorem<br>ipsum is simply</span>
  </div>
  <a class="btn intro-btn abs">Learn More</a>
  <div class="collage abs" style="left:866px;top:818px;width:190px;height:192px" role="img" aria-label="Photo of a woman on the phone at a desk"></div>
  <div class="collage abs" style="left:655px;top:912px;width:193px;height:205px;background:linear-gradient(135deg,#c7b08a,#5a4a3a)" role="img" aria-label="Photo of microphones at a press interview"></div>
  <div class="collage abs" style="left:866px;top:1026px;width:190px;height:192px;background:linear-gradient(135deg,#d7d9dc,#7e8690)" role="img" aria-label="Photo of a team meeting around a table"></div>
  <div class="collage abs" style="left:655px;top:1122px;width:193px;height:193px;background:linear-gradient(135deg,#e3e3e3,#2e3b55)" role="img" aria-label="Photo of a person in a striped top writing notes"></div>
</section>

<h2 class="section-title heading abs" style="left:0;top:1405px">Key Areas of Expertise</h2>
<section class="expertise-grid abs">
  <div class="tile" style="background:linear-gradient(135deg,#5a4040,#2d2424)" role="img" aria-label="Sports media photo background"><h3>Sports Media</h3><span class="btn-outline">Learn More</span></div>
  <div class="tile" style="background:linear-gradient(135deg,#6a4a4e,#352628)" role="img" aria-label="Publicity photo background"><h3>Publicity</h3><span class="btn-outline">Learn More</span></div>
  <div class="tile" style="background:linear-gradient(135deg,#6b6360,#3a3432)" role="img" aria-label="Sponsorship photo background"><h3>Sponsorship Leverage</h3><span class="btn-outline">Learn More</span></div>
  <div class="tile" style="background:linear-gradient(135deg,#6a3f4c,#2e1f28)" role="img" aria-label="Event crowd photo background"><h3>Event Management</h3><span class="btn-outline">Learn More</span></div>
  <div class="tile" style="background:linear-gradient(135deg,#5b6470,#2f3540)" role="img" aria-label="Crisis meeting photo background"><h3>Crisis Management</h3><span class="btn-outline">Learn More</span></div>
  <div class="tile" style="background:linear-gradient(135deg,#44495a,#23263a)" role="img" aria-label="Social media photo background"><h3>Social Media</h3><span class="btn-outline">Learn More</span></div>
  <div class="tile" style="background:linear-gradient(135deg,#5c5e6a,#30323c)" role="img" aria-label="Writing and editing photo background"><h3>Writing &amp; Editing Web, newsletter and magazine content</h3><span class="btn-outline">Learn More</span></div>
  <div class="tile" style="background:linear-gradient(135deg,#665d70,#35303e)" role="img" aria-label="Storytelling photo background"><h3>Storytelling</h3><span class="btn-outline">Learn More</span></div>
</section>

<section class="blog">
  <div class="blog-intro abs">
    <h2>Latest Blog &amp;<br>Updates</h2>
    <p>Contact Mara at VRL for strategic advice on sponsorship spend and how to leverage your investment, and to tap into her extensive media and professional network.</p>
    <a class="btn">Learn More</a>
  </div>
  <article class="post abs" style="left:455px;top:2052px">
    <div class="post-img" style="background:linear-gradient(135deg,#a06a5a,#2f3f66)" role="img" aria-label="Photo of sailors seated at a press conference"></div>
    <p class="post-title">Opinion: Harbour Cup rumbles over with blokes</p>
    <p class="post-meta">May 31st, 2017 by Mara Whitley</p>
    <p class="post-more">READ MORE</p>
  </article>
  <article class="post abs" style="left:767px;top:2052px">
    <div class="post-img" style="background:linear-gradient(135deg,#8a96a6,#2f3a4c)" role="img" aria-label="Photo of a busy media centre"></div>
    <p class="post-title">A normal day in Rio</p>
    <p class="post-meta">August 14th, 2016 by Mara Whitley</p>
    <p class="post-more">READ MORE</p>
  </article>
</section>

<section class="about abs">
  <h2 class="section-title heading">About Us</h2>
  <p class="about-lead heading abs">Mara grew up on Heron Island in Pittwater on Sydney's northern</p>
  <div class="about-text abs">
    <p>Mara grew up on Heron Island in Pittwater on Sydney's northern beaches, the breeding ground for many Australian sailing greats including the Ardens, Coles and the Brennans.</p>
    <p>As a 'tinny terror' she attended Bayview Public School then Northshore High School with some of these sailing families, and now through her work she's back mingling with the greats.</p>
    <p>A communications degree at the University of the Coast, a career that has seen her rise to the top of her specialist field and three children later has brought her full circle back to the island as a home owner.</p>
  </div>
  <div class="pillars abs">
    <div class="pillar">
      <svg width="34" height="30" viewBox="0 0 34 30" aria-hidden="true"><path d="M2 15C8 5 26 5 32 15 26 25 8 25 2 15z" fill="none" stroke="#333" stroke-width="1.6"/><circle cx="17" cy="15" r="5" fill="none" stroke="#333" stroke-width="1.6"/></svg>
      <h4>Our Vision</h4>
      <p>Being a thoughtful mother &amp; partner, running a successful business and being a good friend maintain Mara's busy and well-rounded life.</p>
    </div>
    <div class="pillar">
      <svg width="34" height="30" viewBox="0 0 34 30" aria-hidden="true"><path d="M8 28h18M17 28V4l10 12H17" fill="none" stroke="#333" stroke-width="1.6"/></svg>
      <h4>Our Mission</h4>
      <p>Being a thoughtful mother &amp; partner, running a successful business and being a good friend maintain Mara's busy and well-rounded life.</p>
    </div>
    <div class="pillar">
      <svg width="34" height="30" viewBox="0 0 34 30" aria-hidden="true"><rect x="8" y="3" width="18" height="25" rx="2" fill="none" stroke="#333" stroke-width="1.6"/><path d="M12 14l4 4 7-8" fill="none" stroke="#333" stroke-width="1.6"/></svg>
      <h4>Our Experience</h4>
      <p>Being a thoughtful mother &amp; partner, running a successful business and being a good friend maintain Mara's busy and well-rounded life.</p>
    </div>
  </div>
  <a class="btn about-btn abs">Learn More</a>
</section>

<section class="clients">
  <h2 class="section-title heading abs" style="left:0;top:3050px">Client Portfolio</h2>
  <div class="client-row abs">
    <div class="client-badge" style="width:74px;height:52px"></div>
    <div class="client-badge" style="width:74px;height:74px"></div>
    <div class="client-badge" style="width:54px;height:74px;border-radius:50%"></div>
    <div class="client-badge" style="width:74px;height:60px"></div>
    <div class="client-badge" style="width:64px;height:44px"></div>
    <div class="client-badge" style="width:58px;height:70px"></div>
  </div>
</section>

<footer class="site-footer abs">
  <div class="footer-brand abs">
    <div class="brand-dot"></div>
    <div class="brand-name">Vantage Relations Lab</div>
  </div>
  <div class="footer-social abs"><span class="social-dot"></span><span class="social-dot"></span><span class="social-dot"></span><span class="social-dot"></span></div>
  <ul class="footer-list abs" style="left:410px;top:30px">
    <li>Home</li><li>Services</li><li>About</li><li>Client Portfolio</li><li>Testimonials</li><li>Blog</li><li>Contact</li>
  </ul>
  <ul class="footer-list abs" style="left:556px;top:30px">
    <li>Sports media</li><li>Publicity</li><li>Sponsorship leverage</li><li>Event management</li><li>Crisis management</li><li>Social media</li><li>Writing &amp; editing web</li><li>Storytelling</li>
  </ul>
  <dl class="contact-block abs">
    <div style="margin-bottom:6px">Vantage Relations Lab</div>
    <div><dt>Phone</dt><dd>+61 400 216 730</dd></div>
    <div><dt>Address</dt><dd>PO Box 214, Harbourside NSW 2999 Australia</dd></div>
    <div><dt>Email</dt><dd>mara@vrl.net.au</dd></div>
    <div><dt>ABN</dt><dd>00 123 456 789</dd></div>
  </dl>
  <div class="footer-bottom abs">
    <span>Copyright 2017 All Rights Reserved by Vantage Relations Lab</span>
    <nav><span>Terms &amp; Conditions</span><span>Privacy Policy</span></nav>
  </div>
</footer>

</body>
</html>
```